INCREASED BUDGET -- Cover Art Template Needed For Record Label

We are an electronic music record label that needs a cover art template for our 2017 releases. The design must be easy to update in Photoshop with different text, colors, or patterns.

The winner will also be asked to design our social media banners for Facebook, Twitter, and SoundCloud, so there's an opportunity to make more money.

Words to describe our sound: sophisticated, forward-thinking, futuristic, modern, emotional

Please make the LA logo the focal point of your design. Feel free to modify our logo as needed. Bonus points for anyone that can find a way to visually represent the word "Lanternfold". Examples of artwork that we found attractive are included to provide inspiration.

You can view our previous releases by clicking on any of the links: https://www.tunevaultshop.example/label/lanternfold-audio/52947/releases

Target Market(s)

Electronic music lovers

Industry/Entity Type

Music Download

Font styles to use
Serif
Decorative
Other font styles liked:
• Aller Display, Aller Light

Requirements
Must have
• Lanternfold Audio record logo
• Name of artist: Rufus Delgarde
• Title: Daybreak / Hold Still (Reworks)
Nice to have
• Tracklist:
• Hold Still (Brantlow Remix)
• Daybreak (Zolvarin Remix)
• Catalog number: 318

```html
<!DOCTYPE html>
<html lang="en">
<head>
<meta charset="utf-8">
<title>Rufus Delgarde – Daybreak / Hold Still (Reworks) | Lanternfold Audio</title>
<link href="https://fonts.googleapis.com/css2?family=Cinzel:wght@600;700&display=swap" rel="stylesheet">
<style>
  :root {
    --page-bg: #808080;
    --text-light: #ffffff;
    --art-red: #e0283a;
    --art-red-deep: #8a0f1c;
    --art-pink: #f1a6ae;
    --art-dark: #1a1e24;
    --art-teal: #4f8c9c;
    --art-mist: #d9dde3;
  }
  * { margin: 0; padding: 0; box-sizing: border-box; }
  html, body {
    width: 1200px;
    height: 1000px;
    overflow: hidden;
    background: var(--page-bg);
  }
  .canvas {
    position: relative;
    width: 1200px;
    height: 1000px;
  }
  .cover {
    position: absolute;
    left: 352px;
    top: 252px;
    width: 496px;
    height: 496px;
    overflow: hidden;
    font-family: "Cinzel", "Copperplate", serif;
    color: var(--text-light);
  }
  .cover-artwork {
    position: absolute;
    inset: 0;
    background:
      radial-gradient(circle at 52% 45%, var(--art-red) 0%, rgba(224,40,58,0.6) 22%, transparent 45%),
      radial-gradient(circle at 92% 38%, var(--art-teal) 0%, transparent 22%),
      radial-gradient(circle at 6% 58%, var(--art-mist) 0%, transparent 22%),
      radial-gradient(circle at 78% 85%, var(--art-pink) 0%, var(--art-red) 18%, transparent 42%),
      radial-gradient(circle at 20% 90%, var(--art-pink) 0%, var(--art-red-deep) 25%, transparent 45%),
      radial-gradient(circle at 30% 15%, var(--art-red) 0%, transparent 35%),
      linear-gradient(160deg, var(--art-dark) 0%, var(--art-red-deep) 50%, var(--art-dark) 100%);
  }
  .label-mark {
    position: absolute;
    top: 82px;
    left: 0;
    width: 100%;
    text-align: center;
    font-size: 64px;
    font-weight: 700;
    line-height: 1;
    letter-spacing: 4px;
  }
  .release-text {
    position: absolute;
    top: 206px;
    left: 0;
    width: 100%;
    text-align: center;
  }
  .artist-name {
    font-size: 48px;
    font-weight: 700;
    line-height: 1;
    letter-spacing: 1px;
    text-shadow: 0 0 6px rgba(0,0,0,0.3);
  }
  .release-title {
    margin-top: 6px;
    font-size: 20px;
    font-weight: 700;
    line-height: 1;
    text-shadow: 0 0 4px rgba(0,0,0,0.3);
  }
</style>
</head>
<body>
  <main class="canvas">
    <section class="cover">
      <div class="cover-artwork" role="img" aria-label="Abstract background of red and white light streaks, glowing hexagonal bokeh and faint teal haze on a dark field"></div>
      <div class="label-mark">LA</div>
      <div class="release-text">
        <h1 class="artist-name">Rufus Delgarde</h1>
        <h2 class="release-title">Daybreak / Hold Still (Reworks)</h2>
      </div>
    </section>
  </main>
</body>
</html>
```